Introducing a Personal Care Product called" VELO"

We are a nutra-pharmaceutical company launching a new personal care product called VELO. Some of the products include massage and aroma therapy, as well as personal lubricants. The products will be produced and put into, two bottles that are interlocking so two combinations of products can be purchased at once (i.e. massage and aroma therapy). The poster will be used for promotional advertising, trade shows and for in-store promotions.
Updates

We would like to see a design without the product.

Target Market(s)

Products will be aimed at adults primarily women 18-65 in the USA. We want to appeal to the everyday woman who is interested in their sexual well being.

Industry/Entity Type

Massage

Requirements
Must have
• Clean Presentation. Not many colors. Text should be as follows: VELO for Her....VELO for Him...VELO for You...Let's VELO see attached..Also VELO with Her...Velo with Him..Let's VELO..Open to other copy versions.
Nice to have
• Product image not necessary but can be used. image attached
Should not have
• Too many colors...

```html
<!DOCTYPE html>
<html lang="en">
<head>
<meta charset="utf-8">
<title>velo poster</title>
<link href="https://fonts.googleapis.com/css2?family=Poiret+One&display=swap" rel="stylesheet">
<style>
  :root {
    --pink: #f799c6;
    --blue: #98c9f7;
    --white: #ffffff;
    --ink: #111111;
    --shadow-pink: rgba(160, 30, 90, 0.55);
    --ornament-blue: rgba(120, 170, 230, 0.35);
    --ornament-pink: rgba(235, 140, 190, 0.35);
  }
  html, body {
    margin: 0;
    padding: 0;
    width: 848px;
    height: 1200px;
    overflow: hidden;
    background: var(--white);
  }
  .poster {
    position: relative;
    width: 848px;
    height: 1200px;
    overflow: hidden;
    font-family: "Poiret One", "Century Gothic", sans-serif;
  }
  .backdrop {
    position: absolute;
    inset: 0;
  }
  .ornament {
    position: absolute;
    border-radius: 50%;
    filter: blur(6px);
  }
  .ornament--left {
    left: 20px; top: 40px; width: 260px; height: 780px;
    background: radial-gradient(ellipse at center, var(--ornament-blue), transparent 70%);
  }
  .ornament--top {
    left: 430px; top: 20px; width: 400px; height: 240px;
    background: radial-gradient(ellipse at center, var(--ornament-pink), transparent 70%);
  }
  .tagline {
    position: absolute;
    margin: 0;
    color: var(--white);
    white-space: nowrap;
    line-height: 1;
    text-shadow: 2px 3px 4px var(--shadow-pink);
  }
  .tagline__brand { font-size: 86px; letter-spacing: 1px; }
  .tagline__for { font-size: 46px; margin-left: 8px; }
  .tagline--him { left: 62px; top: 88px; }
  .tagline--her { left: 288px; top: 228px; }
  .tagline--you { left: 478px; top: 370px; }
  .product-area {
    position: absolute;
    left: 240px; top: 500px;
    width: 372px; height: 415px;
    border-radius: 26px 26px 30px 30px;
    background: linear-gradient(90deg, #e9b4c6 0%, #f3e8ee 48%, #e4eef8 52%, #a9d0f2 100%);
    box-shadow: 0 6px 14px rgba(0,0,0,0.18);
  }
  .signoff {
    position: absolute;
    left: 218px; top: 952px;
    margin: 0;
    color: var(--ink);
    white-space: nowrap;
    line-height: 1;
  }
  .signoff__lets { font-size: 64px; }
  .signoff__brand { font-size: 118px; margin-left: 18px; }
  .signoff--reflection {
    transform: scaleY(-1);
    transform-origin: 50% 104px;
    opacity: 0.18;
    -webkit-mask-image: linear-gradient(to top, #000 15%, transparent 60%);
    mask-image: linear-gradient(to top, #000 15%, transparent 60%);
  }
</style>
</head>
<body>
<main class="poster">
  <svg class="backdrop" width="848" height="1200" viewBox="0 0 848 1200" aria-hidden="true">
    <defs>
      <linearGradient id="pink-fade" x1="0" y1="0" x2="0" y2="1">
        <stop offset="0" stop-color="#f799c6"/>
        <stop offset="0.72" stop-color="#f799c6"/>
        <stop offset="0.82" stop-color="#ffffff"/>
        <stop offset="1" stop-color="#f7d3e5"/>
      </linearGradient>
      <linearGradient id="blue-fade" x1="0" y1="0" x2="0" y2="1">
        <stop offset="0" stop-color="#98c9f7"/>
        <stop offset="0.72" stop-color="#98c9f7"/>
        <stop offset="0.82" stop-color="#ffffff"/>
        <stop offset="1" stop-color="#d7e9fb"/>
      </linearGradient>
    </defs>
    <rect class="backdrop__pink" x="0" y="0" width="848" height="1200" fill="url(#pink-fade)"/>
    <path class="backdrop__blue" d="M460 0 C500 250 470 420 425 560 C400 650 420 900 428 1200 L848 1200 L848 0 Z" fill="url(#blue-fade)"/>
  </svg>

  <div class="ornament ornament--left" role="img" aria-label="Faint blue swirling floral flourish"></div>
  <div class="ornament ornament--top" role="img" aria-label="Faint pink swirling floral flourish"></div>

  <p class="tagline tagline--him"><span class="tagline__brand">velo</span><span class="tagline__for">for him</span></p>
  <p class="tagline tagline--her"><span class="tagline__brand">velo</span><span class="tagline__for">for her</span></p>
  <p class="tagline tagline--you"><span class="tagline__brand">velo</span><span class="tagline__for">for you</span></p>

  <div class="product-area" role="img" aria-label="Two interlocking clear bottles, red-capped for her and blue-capped for him, with floral labels"></div>

  <p class="signoff"><span class="signoff__lets">let's</span><span class="signoff__brand">velo</span></p>
  <p class="signoff signoff--reflection" aria-hidden="true"><span class="signoff__lets">let's</span><span class="signoff__brand">velo</span></p>
</main>
</body>
</html>
```